Collectible Card Trading Company ~ Tidewell and Finch Collectibles

Business card design using the attached images as a reference point. The color pallet is the color choice I prefer. If you have any way of improving on the design that would be appreciated. This will be used as an insert for product shipments as well as at geekfair and other collectible trade shows so it needs to be eye catching and memorable. Anything that you can do to make my business POP with this business card would be appreciated.

Target Market(s)

Collectible card purchasers primarily but all collectors ingeneral

Industry/Entity Type

Retail

Contact Information for Business Card

Details are included on the provided images

Colors

Designer to choose colors to be used in the design.

Requirements
Must have
• Bold design
Nice to have
• N/A
Should not have
• N/A

```html
<!DOCTYPE html>
<html lang="en">
<head>
<meta charset="utf-8">
<title>Tidewell &amp; Finch Co. — Business Card</title>
<link rel="stylesheet" href="https://fonts.googleapis.com/css2?family=Saira+Semi+Condensed:wght@600&family=Cinzel:wght@500;700&family=Barlow:wght@500;600;700&display=swap">
<style>
  :root {
    --backdrop: #dcdcdc;
    --slate-light: #575d6c;
    --slate-dark: #464b58;
    --slate-deep: #3d4250;
    --paper: #f7f7f7;
    --copper: #d0823c;
    --ink: #2f3440;
    --white: #ffffff;
  }
  * { margin: 0; padding: 0; box-sizing: border-box; }
  html, body {
    width: 1200px;
    height: 900px;
    overflow: hidden;
    background: var(--backdrop);
  }
  .canvas {
    position: relative;
    width: 1200px;
    height: 900px;
  }
  .card {
    position: absolute;
    left: 384px;
    width: 430px;
    height: 247px;
    overflow: hidden;
    box-shadow: 0 10px 24px rgba(0,0,0,0.22);
  }
  .card--front {
    top: 186px;
    background: linear-gradient(180deg, var(--slate-light), var(--slate-dark));
  }
  .card--back {
    top: 468px;
    display: flex;
  }
  .brand-name {
    position: absolute;
    left: 0;
    right: 0;
    text-align: center;
    font-family: "Saira Semi Condensed", sans-serif;
    font-weight: 600;
    letter-spacing: 0.5px;
  }
  .est, .year {
    position: absolute;
    font-family: "Cinzel", serif;
    font-weight: 700;
  }
  .tagline {
    position: absolute;
    left: 0;
    right: 0;
    text-align: center;
    font-family: "Cinzel", serif;
    font-weight: 700;
    letter-spacing: 0.3px;
  }
  .mascot {
    position: absolute;
    border-radius: 50% 50% 46% 46%;
  }

  /* front */
  .card--front .brand-name { top: 34px; font-size: 30px; color: var(--copper); }
  .card--front .mascot {
    left: 150px; top: 68px; width: 130px; height: 130px;
    background: radial-gradient(circle at 50% 45%, #c98645 0%, #8f6a4d 55%, var(--slate-dark) 100%);
  }
  .card--front .est { left: 74px; top: 150px; font-size: 15px; color: var(--copper); }
  .card--front .year { left: 321px; top: 150px; font-size: 17px; color: var(--copper); }
  .card--front .tagline { top: 210px; font-size: 12px; color: var(--copper); }

  /* back */
  .logo-panel {
    position: relative;
    width: 215px;
    height: 100%;
    background: var(--paper);
  }
  .logo-panel .brand-name { top: 60px; font-size: 17px; color: var(--ink); }
  .logo-panel .mascot {
    left: 70px; top: 88px; width: 74px; height: 76px;
    background: radial-gradient(circle at 50% 45%, #6d717c 0%, #a9abb1 60%, var(--paper) 100%);
  }
  .logo-panel .est { left: 23px; top: 138px; font-size: 8.5px; color: var(--ink); font-weight: 500; }
  .logo-panel .year { left: 166px; top: 137px; font-size: 10px; color: var(--ink); font-weight: 500; }
  .logo-panel .tagline { top: 174px; font-size: 7.5px; color: var(--ink); font-weight: 500; }

  .contact-panel {
    position: relative;
    flex: 1;
    background: linear-gradient(180deg, var(--slate-deep), #363a47);
    padding: 66px 0 0 28px;
    font-family: "Barlow", sans-serif;
  }
  .person-name {
    font-size: 16.5px;
    font-weight: 700;
    color: var(--copper);
    letter-spacing: 0.6px;
    line-height: 1;
  }
  .person-role {
    margin-top: 4px;
    font-size: 9px;
    font-weight: 600;
    color: var(--copper);
    letter-spacing: 0.3px;
  }
  .contact-list {
    list-style: none;
    margin-top: 19px;
  }
  .contact-item {
    display: flex;
    align-items: center;
    height: 17.6px;
    font-size: 11px;
    font-weight: 600;
    color: var(--white);
    letter-spacing: 0.2px;
  }
  .contact-icon {
    flex: none;
    width: 11px;
    height: 11px;
    margin-right: 7px;
  }
</style>
</head>
<body>
<div class="canvas">

  <section class="card card--front">
    <p class="brand-name">Tidewell &amp; Finch Co.</p>
    <div class="mascot" role="img" aria-label="Copper line illustration of a roaring tiger head flanked by lightning bolts"></div>
    <p class="est">EST.</p>
    <p class="year">2016</p>
    <p class="tagline">CARDS &amp; COLLECTIBLES</p>
  </section>

  <section class="card card--back">
    <div class="logo-panel">
      <p class="brand-name">Tidewell &amp; Finch Co.</p>
      <div class="mascot" role="img" aria-label="Dark line illustration of a roaring tiger head flanked by lightning bolts"></div>
      <p class="est">EST.</p>
      <p class="year">2016</p>
      <p class="tagline">CARDS &amp; COLLECTIBLES</p>
    </div>
    <div class="contact-panel">
      <p class="person-name">OWEN HARTLEY JR.</p>
      <p class="person-role">CHIEF COLLECTOR</p>
      <ul class="contact-list">
        <li class="contact-item">
          <svg class="contact-icon" viewBox="0 0 12 12" aria-hidden="true"><circle cx="6" cy="6" r="6" fill="#d0823c"/></svg>
          tidewellfinchco
        </li>
        <li class="contact-item">
          <svg class="contact-icon" viewBox="0 0 12 12" aria-hidden="true"><circle cx="6" cy="6" r="6" fill="#d0823c"/></svg>
          Tidewell_Finch
        </li>
        <li class="contact-item">
          <svg class="contact-icon" viewBox="0 0 12 12" aria-hidden="true">
            <circle cx="6" cy="6" r="6" fill="#d0823c"/>
            <rect x="3" y="4" width="6" height="4.2" fill="#ffffff"/>
            <path d="M3 4 L6 6.4 L9 4" fill="none" stroke="#d0823c" stroke-width="0.8"/>
          </svg>
          owen@tidewellfinchco.com
        </li>
        <li class="contact-item">
          <svg class="contact-icon" viewBox="0 0 12 12" aria-hidden="true">
            <circle cx="6" cy="6" r="6" fill="#d0823c"/>
            <circle cx="6" cy="6" r="3.3" fill="none" stroke="#ffffff" stroke-width="0.8"/>
            <ellipse cx="6" cy="6" rx="1.4" ry="3.3" fill="none" stroke="#ffffff" stroke-width="0.7"/>
            <line x1="2.7" y1="6" x2="9.3" y2="6" stroke="#ffffff" stroke-width="0.7"/>
          </svg>
          www.tidewellfinchco.com
        </li>
      </ul>
    </div>
  </section>

</div>
</body>
</html>
```